Bright Canyon, LLC Business Card Design

We need a product business card designed for a new company Bright Canyon, LLC. We make and resell waterless RV cleaner, polish and protectant. It cleans and protects in a simple spray and wipe step leaving the surface protected and conditioned to repel dust, dirt, water, smudges, bugs and fingerprints while preventing fogging. Safe on acrylic, clarisheet, durvane, plastic, rubber, painted surfaces, chrome, stainless, aluminum, vinyl, leather, glass.... This is an eco-friendly green product.

We want to play off the company name to tell the consumer that the product is easy to use and associate to the nostalgics 1950's in the USA... Thinking old travel trailer with hot rod truck pulling it as the graphic, maybe the husband cleaning the truck and the wife cleaning the trailer for a Bright Canyon surface.
Updates

Just posted our newly finished logo. Need to have "Cleaner and Protectant" added to the design as well. Thanks everyone that has submitted thus far, i am working to get comments on all.

If you need a different file format, please let me know. Thank you.

Most important info, is the logo, website and the words "Cleaner" or "Clean" along "Protectant" or "Protect" the remainder is of less importance. Highlight: www.brightcanyoncleaner.example Focus is on company brand for Brighter Canyon Cleaner product: However, need a section for the following contact info: John Doe (xxx) xxx-xxxx email address Would like space for QR Code if possible.

Target Market(s)

Adults in the USA between ages of 35-75 that are actively involved in the Recreational Vehicle (RV), travel trailer, and hot rod lifestyle. We are targeting the RV marked of the high end travel, 5th wheel and bus RV market. Along with hot rods, automotive and motorcycle market.

Industry/Entity Type

Travel

Requirements
Must have
• Most important info, is the logo, website and the words "Cleaner" or "Clean" along "Protectant" or "Protect" the remainder is of less importance.

Highlight:
www.brightcanyoncleaner.example

Focus is on company brand for Brighter Canyon Cleaner product: However, need a section for the following contact info:

John Doe
(xxx) xxx-xxxx
email address
Nice to have
• Would like a space for a QR Code.

```html
<!DOCTYPE html>
<html lang="en">
<head>
<meta charset="utf-8">
<title>Bright Canyon, LLC – Business Card</title>
<link rel="stylesheet" href="https://fonts.googleapis.com/css2?family=Jost:wght@300;400&family=Tinos:wght@400;700&display=swap">
<style>
  :root {
    --navy: #0d2c8c;
    --navy-deep: #0a2276;
    --royal: #1d4fb0;
    --gold: #f1b018;
    --paper: #f7fbfc;
    --stage: #e9ebee;
    --shadow: rgba(10, 20, 60, 0.25);
  }
  * { box-sizing: border-box; margin: 0; padding: 0; }
  html, body {
    width: 1200px;
    height: 960px;
    overflow: hidden;
    background: var(--stage);
  }
  .stage {
    width: 1200px;
    height: 960px;
    display: flex;
    flex-direction: column;
    align-items: center;
    justify-content: center;
    gap: 56px;
  }
  .card {
    position: relative;
    width: 700px;
    height: 400px;
    border-radius: 22px;
    overflow: hidden;
    box-shadow: 0 14px 34px var(--shadow);
  }
  .brand {
    font-family: "Jost", sans-serif;
    font-weight: 300;
    letter-spacing: 0.5px;
    white-space: nowrap;
    line-height: 1.1;
  }
  .tagline {
    font-family: "Jost", sans-serif;
    font-weight: 400;
    letter-spacing: 3px;
    text-transform: uppercase;
    white-space: nowrap;
  }

  /* Front */
  .card--front {
    background: linear-gradient(160deg, var(--royal) 0%, var(--navy) 55%, var(--navy-deep) 100%);
    display: flex;
    flex-direction: column;
    align-items: center;
    justify-content: center;
    gap: 14px;
    color: #ffffff;
  }
  .card--front .brand { font-size: 64px; }
  .card--front .tagline { font-size: 20px; color: var(--gold); }
  .card--front .site {
    font-family: "Jost", sans-serif;
    font-weight: 400;
    font-size: 22px;
    margin-top: 10px;
  }

  /* Back */
  .card--back { background: var(--navy); }
  .back__top {
    position: absolute;
    left: 0; top: 0;
    width: 100%;
    height: 168px;
    background: var(--paper);
    display: flex;
    flex-direction: column;
    justify-content: flex-end;
    padding: 0 0 22px 40px;
    gap: 6px;
  }
  .card--back .brand { color: var(--navy); font-size: 56px; }
  .card--back .tagline { color: var(--navy); font-size: 16px; }
  .back__stripe {
    position: absolute;
    left: 0; top: 168px;
    width: 100%;
    height: 14px;
    background: var(--gold);
  }
  .contact {
    position: absolute;
    left: 290px;
    top: 204px;
    width: 380px;
    font-family: "Tinos", serif;
    color: #ffffff;
  }
  .contact__name {
    font-weight: 700;
    font-size: 22px;
    letter-spacing: 1px;
    text-transform: uppercase;
  }
  .contact__role {
    font-size: 16px;
    margin: 2px 0 12px;
  }
  .contact__lines {
    list-style: none;
    font-size: 16px;
    line-height: 1.45;
  }
  .contact__lines .site {
    font-weight: 700;
    color: var(--gold);
    font-size: 17px;
  }
</style>
</head>
<body>
<main class="stage">
  <section class="card card--front" aria-label="Business card front">
    <h1 class="brand">Bright Canyon, LLC</h1>
    <p class="tagline">Cleaner and Protectant</p>
    <p class="site">www.brightcanyoncleaner.example</p>
  </section>

  <section class="card card--back" aria-label="Business card back">
    <div class="back__top">
      <p class="brand">Bright Canyon, LLC</p>
      <p class="tagline">Cleaner and Protectant</p>
    </div>
    <div class="back__stripe"></div>
    <div class="contact">
      <p class="contact__name">Jonathan Doe</p>
      <p class="contact__role">Managing Director</p>
      <ul class="contact__lines">
        <li>0012 3456 789</li>
        <li>info@youremail.com</li>
        <li class="site">www.brightcanyoncleaner.example</li>
        <li>Your Adress Inc 2nd Lane Ave<br>Maple Hollow, NJ 00000</li>
      </ul>
    </div>
  </section>
</main>
</body>
</html>
```